Business Card Design Project

We are a construction company in Orange County, CA. We need a two sided business card. We would like the back to be our logo with web URL. Front should included Name, title, address, phone, fax and email address.

our address is
387 West Marlowe Blvd, Suite 402
Anaheim, CA 92805

Our logo files are attached.

Construction

```html
<!DOCTYPE html>
<html lang="en">
<head>
<meta charset="utf-8">
<title>Keystone Business Card</title>
<link rel="stylesheet" href="https://fonts.googleapis.com/css2?family=Open+Sans:wght@400;600;700;800&family=PT+Serif:wght@700&display=swap">
<style>
  :root {
    --brand-blue: #1b4a7c;
    --accent-gray: #7a7a7a;
    --card-light: #ffffff;
    --card-shade: #e4e4e6;
    --ink-dark: #2b2b2b;
    --strip-light: #ebebed;
  }
  * { box-sizing: border-box; margin: 0; padding: 0; }
  html, body { width: 998px; height: 1200px; overflow: hidden; background: #ffffff; }
  .canvas { position: relative; width: 998px; height: 1200px; font-family: "Open Sans", Arial, sans-serif; }

  .edge-bar { position: absolute; left: 0; width: 998px; height: 18px; display: flex; }
  .edge-bar .blue { width: 713px; background: var(--brand-blue); }
  .edge-bar .gray { flex: 1; background: var(--accent-gray); }

  .card { position: absolute; left: 0; width: 998px; overflow: hidden;
          background: radial-gradient(ellipse at 50% 40%, var(--card-light) 0%, #f4f4f5 55%, var(--card-shade) 100%); }
  .card-front { top: 15px; height: 600px; }
  .card-back { top: 637px; height: 545px; }

  .company-name { position: absolute; left: 0; width: 100%; text-align: center;
                  color: var(--brand-blue); font-weight: 800; line-height: 1; letter-spacing: 2px; }
  .card-front .company-name { top: 55px; font-size: 140px; }
  .card-back .company-name { top: 128px; font-size: 122px; }

  .person { position: absolute; left: 58px; top: 325px; }
  .person-name { font-size: 37px; font-weight: 600; color: var(--brand-blue);
                 padding-bottom: 4px; border-bottom: 2px solid #b9c3cf; width: 290px; line-height: 1.25; }
  .person-title { font-size: 25px; font-weight: 700; color: var(--ink-dark); margin-top: 4px; }

  .contact { position: absolute; right: 66px; top: 322px; text-align: right;
             font-size: 24px; color: var(--ink-dark); line-height: 38px; font-weight: 600; }

  .address-band { position: absolute; left: 0; top: 495px; width: 998px; height: 66px;
                  background: var(--brand-blue); color: #ffffff; font-size: 26px;
                  display: flex; align-items: center; justify-content: center; }

  .web-strip { position: absolute; left: 90px; top: 333px; width: 818px; height: 43px;
               background: linear-gradient(90deg, rgba(235,235,237,0) 0%, var(--strip-light) 20%, var(--strip-light) 80%, rgba(235,235,237,0) 100%);
               display: flex; align-items: center; justify-content: center;
               font-family: "PT Serif", Georgia, serif; font-weight: 700; font-size: 26px; color: var(--brand-blue); }
</style>
</head>
<body>
<div class="canvas">
  <div class="edge-bar" style="top:0"><div class="blue"></div><div class="gray"></div></div>

  <section class="card card-front">
    <div class="company-name">KEYSTONE</div>
    <div class="person">
      <div class="person-name">Name of Person</div>
      <div class="person-title">Person Designation</div>
    </div>
    <div class="contact">
      <div>Phone : +61555010246</div>
      <div>Fax : +44 161 555 0172</div>
      <div>Email : info@keystonebuild.com</div>
    </div>
    <div class="address-band">Address : 387 West Marlowe Blvd, Suite 402 Anaheim, CA 92805</div>
  </section>

  <div class="edge-bar" style="top:619px"><div class="blue"></div><div class="gray"></div></div>

  <section class="card card-back">
    <div class="company-name">KEYSTONE</div>
    <div class="web-strip">http://www.keystonebuild.com</div>
  </section>

  <div class="edge-bar" style="top:1182px"><div class="blue"></div><div class="gray"></div></div>
</div>
</body>
</html>
```